Business Cards & Stationary for Solo Attorney
Marcus Tolland Counsellor At Law
Business Cards & Stationary for Solo Attorney - Law
Creative Brief
Professional
Marcus Tolland
Counsellor At Law
482 Brindlecombe Avenue, 5th Floor Harwick, Vermont 08347
mtollandlaw@quillpost.example
tollandlawfirm.example

```html
<!DOCTYPE html>
<html lang="en">
<head>
<meta charset="utf-8">
<title>Marcus Tolland — Business Cards</title>
<link rel="stylesheet" href="https://fonts.googleapis.com/css2?family=Cinzel:wght@400;600&display=swap">
<style>
  :root {
    --canvas-bg: #e9e6e2;
    --card-bg: #565656;
    --ink-light: #f2f2f2;
    --ink-soft: #d6d6d6;
    --band: #ffffff;
    --ink-dark: #3e3e3e;
  }
  * { margin: 0; padding: 0; box-sizing: border-box; }
  html, body {
    width: 1200px; height: 850px; overflow: hidden;
    background: var(--canvas-bg);
    font-family: "Cinzel", serif;
  }
  .canvas { position: relative; width: 1200px; height: 850px; }
  .card {
    position: absolute; top: 319px;
    width: 362px; height: 206px;
    background: var(--card-bg);
    box-shadow: 0 3px 10px rgba(0,0,0,0.25);
    color: var(--ink-light);
  }
  .card--front { left: 139px; }
  .card--back { left: 703px; }
  .card__frame {
    position: absolute; inset: 7px;
    border: 1px solid rgba(255,255,255,0.55);
  }
  .brand-mark {
    position: absolute;
    border-radius: 50%;
    border: 2px solid var(--ink-light);
  }
  .card--front .brand-mark { top: 56px; left: 158px; width: 46px; height: 46px; }
  .card--back .brand-mark { top: 22px; left: 232px; width: 40px; height: 40px; }
  .front-name {
    position: absolute; top: 114px; width: 100%; text-align: center;
    font-size: 22px; letter-spacing: 1px; font-weight: 400; line-height: 28px;
  }
  .front-title {
    position: absolute; top: 145px; width: 100%; text-align: center;
    font-size: 8.5px; letter-spacing: 1.5px; color: var(--ink-soft);
  }
  .front-title::before, .front-title::after {
    content: ""; display: inline-block; width: 22px; height: 1px;
    background: var(--ink-soft); vertical-align: middle; margin: 0 5px;
  }
  .name-band {
    position: absolute; top: 101px; left: 142px; right: 0; height: 19px;
    background: var(--band); color: var(--ink-dark);
    font-size: 12px; font-weight: 400; letter-spacing: 1px; line-height: 19px;
    text-align: center;
  }
  .back-title {
    position: absolute; top: 124px; left: 142px; right: 0; text-align: center;
    font-size: 7px; letter-spacing: 1px; color: var(--ink-soft);
  }
  .contact {
    position: absolute; top: 154px;
    font-size: 7.5px; line-height: 12px; letter-spacing: 0.4px;
    color: var(--ink-light); list-style: none; white-space: nowrap;
  }
  .contact--phone { left: 9px; }
  .contact--office { left: 172px; }
</style>
</head>
<body>
<main class="canvas">
  <section class="card card--front">
    <div class="card__frame"></div>
    <div class="brand-mark" role="img" aria-label="Marcus Tolland emblem"></div>
    <h1 class="front-name">Marcus Tolland</h1>
    <p class="front-title">Counsellor At Law</p>
  </section>

  <section class="card card--back">
    <div class="brand-mark" role="img" aria-label="Marcus Tolland emblem"></div>
    <h2 class="name-band">Marcus Tolland</h2>
    <p class="back-title">Counsellor At Law</p>
    <ul class="contact contact--phone">
      <li>Ph : (608) 555-0142</li>
      <li>Fax : (608) 555-0187</li>
      <li>www.tollandlawfirm.example</li>
    </ul>
    <ul class="contact contact--office">
      <li>mtollandlaw@quillpost.example</li>
      <li>482 Brindlecombe Avenue, 5th Floor</li>
      <li>Harwick, Vermont 08347</li>
    </ul>
  </section>
</main>
</body>
</html>
```